Clean Air Information

I am uploading a rough draft on what I want. I am looking for different ideas on how to make it look more attractive and not so boring. I want it to really stand out and make a statement. Also, I am uploading additional documents for statement information or additional use.

Reason: I am providing more time to ensure there is enough time for all parties.

The most recent submissions are looking good. Please keep it coming, I have extended deadline.

```html
<!DOCTYPE html>
<html lang="en">
<head>
<meta charset="utf-8">
<title>Let us help you breathe easier</title>
<link rel="stylesheet" href="https://fonts.googleapis.com/css2?family=Arimo:wght@400;700&display=swap">
<style>
  :root {
    --green: #3aa655;
    --green-dark: #2f9a4a;
    --orange: #f07022;
    --yellow: #f6b21a;
    --ink: #222222;
    --paper: #ffffff;
    --fold: #e6e6e6;
    --photo-grey: #b9b9b3;
  }
  * { box-sizing: border-box; margin: 0; padding: 0; }
  html, body { width: 1200px; height: 927px; overflow: hidden; background: var(--paper); }
  body { font-family: "Arimo", Arial, sans-serif; color: var(--ink); }
  .brochure { position: relative; width: 1200px; height: 927px; overflow: hidden; background: var(--paper); }
  .fold { position: absolute; top: 0; bottom: 0; width: 1px; background: var(--fold); }
  .fold--one { left: 399px; }
  .fold--two { left: 800px; }

  .waves { position: absolute; left: 0; top: 0; width: 1200px; height: 927px; z-index: 1; }

  .panel { position: absolute; top: 0; z-index: 2; font-size: 13.4px; line-height: 16.8px; }
  .panel--left { left: 49px; width: 345px; }
  .panel--middle { left: 444px; width: 312px; }
  .panel--right { left: 840px; width: 318px; }

  .brand { position: absolute; left: -16px; top: 60px; display: flex; align-items: center; gap: 14px; }
  .brand__mark { width: 78px; height: 78px; border-radius: 50%; border: 6px solid var(--green); flex: none; }
  .brand__tagline { color: var(--green); font-size: 34px; line-height: 36px; font-weight: 400; }
  .brand__name { position: absolute; left: 0; top: 90px; color: var(--green); font-size: 11px; font-weight: 400; letter-spacing: .5px; }

  .heading { color: var(--orange); font-size: 19.5px; font-weight: 700; line-height: 22px; }
  .step { color: var(--green); font-size: 13.4px; font-weight: 700; line-height: 16.8px; }
  .step::before, .offer-list li::before {
    content: ""; display: inline-block; width: 0; height: 0; margin-right: 6px;
    border-top: 5px solid transparent; border-bottom: 5px solid transparent; border-left: 6px solid var(--green);
    vertical-align: -1px;
  }

  .intro { position: absolute; top: 171px; }
  .intro .heading { margin-bottom: 2px; }
  .intro__lungs { float: left; width: 140px; height: 120px; margin: 10px 8px 4px 0; border-radius: 40% 40% 30% 30%;
    background: radial-gradient(ellipse at 50% 40%, #cfe7f5 0%, #9cc9e6 70%, #eaf4fb 100%); }

  .furnace { position: absolute; left: -27px; top: 469px; width: 372px; height: 360px; border-radius: 6px;
    background: linear-gradient(160deg, #c9d4e2 0%, #8fa6c2 55%, #dfe5ec 100%); }

  .offers { position: absolute; top: 60px; }
  .offer-list { list-style: none; margin-top: 3px; }
  .offer-list li { line-height: 16.7px; }

  .process { position: absolute; top: 299px; }
  .process p { margin-bottom: 0; }

  .photo { position: absolute; border-radius: 50%; border: 3px solid #fff; box-shadow: 0 0 0 1px #ddd; z-index: 2; }
  .photo--vent { left: 410px; top: 490px; width: 210px; height: 210px; background: radial-gradient(circle, #f2f2f0 0%, #cfd0cc 100%); }
  .photo--mold { left: 577px; top: 468px; width: 175px; height: 175px; background: radial-gradient(circle at 45% 50%, #8a7a3a 0%, #a9a99f 45%, #7d7f7c 100%); }
  .photo--duct { left: 410px; top: 674px; width: 175px; height: 175px; background: radial-gradient(circle, #b6b79c 0%, #8e9177 70%, #c9c9b6 100%); }
  .photo--worker { left: 580px; top: 614px; width: 245px; height: 245px; background: linear-gradient(160deg, #9b7a4a 0%, #d8d6d2 45%, #eeeeee 100%); }

  .steps { position: absolute; top: 62px; }
  .keep { position: absolute; top: 311px; }
  .cost { position: absolute; top: 482px; }
  .keep .heading, .cost .heading { margin-bottom: 1px; }

  .contact { position: absolute; left: 800px; width: 400px; top: 810px; z-index: 3; text-align: center; color: #fff; }
  .contact__phone { font-size: 27px; line-height: 32px; }
  .contact__web { font-size: 28px; line-height: 34px; }
</style>
</head>
<body>
<main class="brochure">
  <div class="fold fold--one"></div>
  <div class="fold fold--two"></div>

  <svg class="waves" viewBox="0 0 1200 927" aria-hidden="true">
    <!-- left and middle panel base -->
    <path d="M0 812 C160 790 330 800 480 850 C600 890 700 880 800 840 L800 927 L0 927 Z" fill="var(--yellow)"/>
    <path d="M0 820 C170 800 330 812 470 858 C590 898 700 890 800 852 L800 927 L0 927 Z" fill="var(--paper)"/>
    <path d="M0 832 C170 812 330 826 460 870 C580 910 700 904 800 870 L800 927 L0 927 Z" fill="var(--green)"/>
    <!-- right panel sweep -->
    <path d="M800 820 C900 780 1000 730 1200 705 L1200 927 L800 927 Z" fill="var(--orange)"/>
    <path d="M800 840 C910 800 1010 755 1200 742 L1200 927 L800 927 Z" fill="var(--green)"/>
  </svg>

  <section class="panel panel--left">
    <div class="brand">
      <div class="brand__mark"></div>
      <h1 class="brand__tagline">Let us help you<br>breathe easier</h1>
      <span class="brand__name">ClearVent Air</span>
    </div>

    <div class="intro">
      <h2 class="heading">What We Can Do for you</h2>
      <div class="intro__lungs" role="img" aria-label="Illustration of human lungs"></div>
      <p>Picture your HVAC system as the lungs of your house; it takes air in and breathes air out, and if the airways are contaminated, the air that gets breathed out will be infused with those contaminants. As with your own health, an ounce of prevention is worth a pound of cure, and catching any existing issues early can make all the difference in the world. Keeping your HVAC system clean and free of contaminants not only improves the air quality in your home, it can improve the quality of life for those in your household.</p>
    </div>

    <div class="furnace" role="img" aria-label="Cutaway diagram of a home furnace and duct system showing airflow"></div>
  </section>

  <section class="panel panel--middle">
    <div class="offers">
      <h2 class="heading">We offer</h2>
      <ul class="offer-list">
        <li>HVAC Inspection</li>
        <li>Mold Testing</li>
        <li>Air Duct Cleaning</li>
        <li>Contaminant Removal</li>
        <li>Air Quality Assessment and Protocol</li>
        <li>Mold Mitigation and Remediation</li>
        <li>HVAC Remediation/Replacement</li>
        <li>Water and Fire Damage Restoration</li>
        <li>Reconstruction</li>
        <li>Catastrophe Relief Coordination</li>
        <li>After Hours Emergency Service</li>
        <li>Insurance Advocate Services</li>
      </ul>
    </div>

    <div class="process">
      <h2 class="heading">Our process</h2>
      <h3 class="step">Inspection and Testing</h3>
      <p>A thorough inspection is performed and samples are taken and sent out for 3rd party testing to determine category and severity level. A proper protocol for your home is developed from this report.</p>
      <h3 class="step">Dehumidification</h3>
      <p>Any standing water or water damage in your home is cleaned out and all affected areas are thoroughly dried.</p>
    </div>
  </section>

  <div class="photo photo--vent" role="img" aria-label="Photo of a white air return vent grille"></div>
  <div class="photo photo--mold" role="img" aria-label="Photo of mold growth on a metal HVAC panel"></div>
  <div class="photo photo--duct" role="img" aria-label="Photo of a dusty flexible air duct"></div>
  <div class="photo photo--worker" role="img" aria-label="Photo of a technician in protective suit cleaning a ceiling"></div>

  <section class="panel panel--right">
    <div class="steps">
      <h3 class="step">Containment</h3>
      <p>Chambers can be placed around localized areas to prevent any further migration until the areas have been thoroughly decontaminated.</p>
      <h3 class="step">Removal and Replacement</h3>
      <p>If any components cannot be restored, they will be safely removed from the premises and replaced.</p>
      <h3 class="step">Disinfection</h3>
      <p>A detailed cleaning and disinfection of all the components and ductwork within your system will be performed.</p>
      <h3 class="step">Confirmation</h3>
      <p>Retest of the system and the air in your home to verify that the contaminants have been eradicated.</p>
    </div>

    <div class="keep">
      <h2 class="heading">Keep in mind</h2>
      <p>Even if you are not concerned with possibly having mold growth in your home, it is still a good idea to keep your HVAC system cleaned out. Other allergens besides mold, such as pollens, dust, and pet dander get picked up by HVAC systems and can get recycled through the house up to 5-7 times a day.</p>
    </div>

    <div class="cost">
      <h2 class="heading">Cost Effective</h2>
      <p>Additionally, according the US Department of Energy, 25-40% of the energy used for heating and cooling is wasted due to contaminants within they system causing it to work harder and ultimately shortening the life of the system. If you’ve been noticing that your system is not as efficient as it once was, it may be due to buildup in either your unit or ductwork. Maintaining the cleanliness of your system may not only help to lower your monthly electric bills, but it could possibly save you the cost and headache of replacing your heating or cooling unit altogether</p>
    </div>
  </section>

  <div class="contact">
    <p class="contact__phone">555-014-2287</p>
    <p class="contact__web">www.clearvent-air.com</p>
  </div>
</main>
</body>
</html>
```